New Zealand Marlborough Sauvignon Blanc wine packaging design

We need packaging design for our new wine brand, Halloway Brisk. The wine is a New Zealand Marlborough Sauvignon Blanc. We would like the packaging will portray elegance and style with an understated label. We are looking for a label that portrays the elegance of the French Riviera. The label should be round or pill shaped.

Industry/Entity Type

Wine

Font styles to use
Serif
Sans Serif

Requirements
Must have
• The words in order of importance: Halloway Brisk, Sauvignon Blanc, Marlborough, New Zealand. It should be fit to the bottle posted in the links
Nice to have
• a pill shape or circular shape
Should not have
• Illustrations of wine bottles, wine glasses, or grapes

```html
<!DOCTYPE html>
<html lang="en">
<head>
<meta charset="utf-8">
<title>Halloway Brisk Sauvignon Blanc – Label</title>
<link href="https://fonts.googleapis.com/css2?family=Cinzel:wght@400&family=Montserrat:wght@700&family=Cormorant+Garamond:wght@500&display=swap" rel="stylesheet">
<style>
  :root {
    --page-bg: #ffffff;
    --label-paper: #ffffff;
    --label-border: #0a0a0a;
    --label-inner-ring: #8a8a8a;
    --ink: #111111;
    --ink-soft: #6a6a6a;
    --scene-light: #f1f1f1;
    --scene-mid: #b9b9b9;
    --scene-dark: #8c8c8c;
  }
  html, body {
    margin: 0;
    padding: 0;
    width: 1006px;
    height: 1200px;
    overflow: hidden;
    background: var(--page-bg);
  }
  .label-canvas {
    width: 1006px;
    height: 1200px;
    display: block;
  }
  .label-paper { fill: var(--label-paper); }
  .label-border { fill: none; stroke: var(--label-border); stroke-width: 14; }
  .label-inner-ring { fill: none; stroke: var(--label-inner-ring); stroke-width: 5; }
  .brand-name {
    font-family: "Cinzel", "Times New Roman", serif;
    font-size: 64px;
    letter-spacing: 4px;
    fill: var(--ink);
  }
  .varietal {
    font-family: "Montserrat", Arial, sans-serif;
    font-weight: 700;
    font-size: 36px;
    fill: var(--ink);
  }
  .region {
    font-family: "Cormorant Garamond", Georgia, serif;
    font-weight: 500;
    font-size: 24px;
    letter-spacing: 1px;
    fill: var(--ink-soft);
  }
  .country {
    font-family: "Cormorant Garamond", Georgia, serif;
    font-weight: 500;
    font-size: 32px;
    letter-spacing: 2px;
    fill: var(--ink);
  }
</style>
</head>
<body>
<svg class="label-canvas" viewBox="0 0 1006 1200" xmlns="http://www.w3.org/2000/svg">
  <defs>
    <clipPath id="label-shape">
      <ellipse cx="503" cy="600" rx="410" ry="340"/>
    </clipPath>
    <linearGradient id="harbour-tones" x1="0" y1="0" x2="0" y2="1">
      <stop offset="0" stop-color="var(--scene-light)"/>
      <stop offset="0.35" stop-color="var(--scene-mid)"/>
      <stop offset="0.6" stop-color="var(--scene-light)"/>
      <stop offset="1" stop-color="var(--scene-dark)"/>
    </linearGradient>
    <path id="brand-arc" d="M 170 560 A 340 290 0 0 1 836 560"/>
  </defs>

  <g class="wine-label">
    <ellipse class="label-paper" cx="503" cy="600" rx="430" ry="360"/>

    <g class="harbour-scene" role="img" aria-label="Sketched Riviera harbour with waterfront houses, a bell tower and moored wooden boats" clip-path="url(#label-shape)">
      <rect x="130" y="490" width="740" height="330" rx="40" fill="url(#harbour-tones)" opacity="0.85"/>
    </g>

    <text class="brand-name">
      <textPath href="#brand-arc" startOffset="50%" text-anchor="middle">HALLOWAY BRISK</textPath>
    </text>
    <text class="varietal" x="520" y="420" text-anchor="middle">SAUVIGNON BLANC</text>
    <text class="region" x="560" y="452" text-anchor="middle">MARLBOROUGH,</text>
    <text class="country" x="503" y="882" text-anchor="middle">NEW ZEALAND</text>

    <ellipse class="label-inner-ring" cx="503" cy="600" rx="414" ry="344"/>
    <ellipse class="label-border" cx="503" cy="600" rx="430" ry="360"/>
  </g>
</svg>
</body>
</html>
```